Autodetailing namecard design: Rose Gold Lettering on Black Matt

This is a namecard design project
requiring two-sided design
Base Color of Namecard: black matt

On front:
Company name,
"Lumira Finishes 46 Kenanga"
Subtext: Auto Detailing Studio

Name of card holder: Darren Lim
Phone Number: +6011-4027-8853
address: 46, Jalan Kenanga 5/3Taman Seri Kenanga, 81300 Johor Bahru, Johor, Malaysia

Back:
Our Services
High Gloss Car Paint Protection
Custom Color Modification and Styling
Anti-Chip Glass Protection Film
Heat Rejection Glass Tinting

Target Market(s)

Autodetailing for highend cars

Contact Information for Business Card

as mentioned in project details

Colors

Designer to choose colors to be used in the design.

Requirements
Must have
• The main value-add to this project is the design of a logo suited for our purpose and name, and the inclusion of business card details into the card design

```html
<!DOCTYPE html>
<html lang="en">
<head>
<meta charset="utf-8">
<title>Lumira Finishes 46 Kenanga – Business Card</title>
<link href="https://fonts.googleapis.com/css2?family=Aldrich&family=Roboto:wght@400&display=swap" rel="stylesheet">
<style>
  :root {
    --backdrop: #6a6a6a;
    --card-black: #1c1b1b;
    --rose-gold: #c49a85;
    --rose-gold-soft: #b58c78;
    --service-text: #c9c9c9;
  }
  html, body {
    margin: 0;
    padding: 0;
    width: 1200px;
    height: 512px;
    overflow: hidden;
    background: var(--backdrop);
  }
  .canvas {
    position: relative;
    width: 1200px;
    height: 512px;
  }
  .card {
    position: absolute;
    top: 139px;
    width: 388px;
    height: 234px;
    background: var(--card-black);
    border-radius: 10px;
  }
  .card--front { left: 202px; }
  .card--back { left: 610px; }

  /* Front: brand lockup */
  .brand-lockup {
    position: absolute;
    left: 46px;
    top: 40px;
    width: 294px;
    height: 42px;
    box-sizing: border-box;
    border: 1px solid var(--rose-gold);
    border-bottom: none;
  }
  .brand-lockup__name {
    font-family: "Aldrich", sans-serif;
    font-size: 18px;
    color: var(--rose-gold);
    text-align: center;
    line-height: 40px;
    letter-spacing: 0.2px;
    white-space: nowrap;
  }
  .brand-lockup__tagline {
    position: absolute;
    left: -1px;
    right: -1px;
    bottom: -6px;
    display: flex;
    align-items: center;
    gap: 8px;
    font-family: "Roboto", sans-serif;
    font-size: 10.5px;
    letter-spacing: 0.6px;
    color: var(--rose-gold);
    white-space: nowrap;
  }
  .brand-lockup__tagline::before,
  .brand-lockup__tagline::after {
    content: "";
    flex: 1;
    height: 1px;
    background: var(--rose-gold);
  }
  .brand-lockup__tagline::before { flex: 0 0 56px; }
  .brand-lockup__tagline::after { flex: 0 0 56px; }

  .holder-name {
    position: absolute;
    left: 0;
    right: 0;
    top: 112px;
    text-align: center;
    font-family: "Aldrich", sans-serif;
    font-size: 19px;
    color: var(--rose-gold);
  }
  .contact {
    position: absolute;
    left: 0;
    right: 0;
    top: 153px;
    text-align: center;
    font-family: "Roboto", sans-serif;
    font-size: 9.5px;
    line-height: 15px;
    color: var(--rose-gold-soft);
  }

  /* Back */
  .services-title {
    position: absolute;
    left: 28px;
    top: 24px;
    margin: 0;
    font-family: "Aldrich", sans-serif;
    font-weight: 400;
    font-size: 17.5px;
    color: var(--rose-gold);
  }
  .services-list {
    position: absolute;
    left: 28px;
    top: 137px;
    margin: 0;
    padding: 0;
    list-style: none;
    font-family: "Roboto", sans-serif;
    font-size: 10px;
    color: var(--service-text);
  }
  .services-list li {
    height: 20px;
    line-height: 16px;
  }
  .services-list li::before {
    content: "»";
    margin-right: 6px;
  }
  .brand-vertical {
    position: absolute;
    left: 228px;
    top: 103px;
    width: 200px;
    height: 28px;
    box-sizing: border-box;
    border: 1px solid var(--rose-gold-soft);
    transform: rotate(-90deg);
    text-align: center;
    white-space: nowrap;
  }
  .brand-vertical__name {
    font-family: "Aldrich", sans-serif;
    font-size: 11.5px;
    line-height: 14px;
    padding-top: 1px;
    color: var(--rose-gold);
  }
  .brand-vertical__tagline {
    font-family: "Roboto", sans-serif;
    font-size: 7px;
    letter-spacing: 0.5px;
    line-height: 9px;
    color: var(--rose-gold-soft);
  }
</style>
</head>
<body>
<main class="canvas">
  <section class="card card--front" aria-label="Card front">
    <div class="brand-lockup">
      <div class="brand-lockup__name">Lumira Finishes 46 Kenanga</div>
      <div class="brand-lockup__tagline">AUTO DETAILING STUDIO</div>
    </div>
    <div class="holder-name">Darren Lim</div>
    <div class="contact">
      +6011-4027-8853<br>
      46, Jalan Kenanga 5/3Taman Seri Kenanga,<br>
      81300 Johor Bahru, Johor, Malaysia
    </div>
  </section>

  <section class="card card--back" aria-label="Card back">
    <h2 class="services-title">Our Services</h2>
    <ul class="services-list">
      <li>High Gloss Car Paint Protection</li>
      <li>Custom Color Modification and Styling</li>
      <li>Anti-Chip Glass Protection Film</li>
      <li>Heat Rejection Glass Tinting</li>
    </ul>
    <div class="brand-vertical">
      <div class="brand-vertical__name">Lumira Finishes 46 Kenanga</div>
      <div class="brand-vertical__tagline">AUTO DETAILING STUDIO</div>
    </div>
  </section>
</main>
</body>
</html>
```